Business Card Design Project

I need a new business card design for my Remodel/Design/Build company, Brightfield Renovation Works, Inc. See our website: www.brightfieldrenovationworks.com
We are an established company with a growing reputation and growing quickly. We are know for being on the forward edge of the industry, producing a great product and our "people friendly" approach.
I am looking for something cool, transitional, maybe even retro that captures the imagination, shows our sleek creativity and streamlined approach as well as communicates stability and trustworthiness.
Updates

Stainless steel business card design would be cool.

Please have all future designs with full logo colors and shown on a stainless steel business card.  Also, logo and tag line will most likely be printed with spot uv, so layers will be necessary.  Thank you.

Target Market(s)

30-65 yrs old, homeowners, appreciate fine things, median income $150+k, net worth $1+m

Industry/Entity Type

Business

Requirements
Must have
• Company Logo
Contact information
Website URL
Nice to have
• Tagline: Crafting Lasting Trust and Renewing Houses...One Family at a Time.
Double-sided okay.
Stainless steel business card.

```html
<!DOCTYPE html>
<html lang="en">
<head>
<meta charset="utf-8">
<title>Brightfield Renovation Works – Business Card Front</title>
<link rel="stylesheet" href="https://fonts.googleapis.com/css2?family=Montserrat:wght@700&family=Fira+Sans+Extra+Condensed:wght@400;600&family=Courgette&family=Roboto:ital,wght@0,500;1,400&display=swap">
<style>
  :root {
    --page: #ffffff;
    --steel: #b1b2ad;
    --ink: #5a5a58;
    --mark: #ffffff;
    --label: #111111;
  }
  * { margin: 0; padding: 0; box-sizing: border-box; }
  html, body { width: 1200px; height: 1000px; overflow: hidden; background: var(--page); }
  .sheet { position: relative; width: 1200px; height: 1000px; }

  .card {
    position: absolute; left: 127px; top: 202px;
    width: 995px; height: 568px;
    background: var(--steel);
    overflow: hidden;
  }
  .wordmark { position: absolute; left: 0; top: 0; width: 995px; height: 568px; }
  .wordmark text { font-family: "Montserrat", sans-serif; font-weight: 700; fill: var(--mark); }

  .holder { position: absolute; right: 45px; top: 240px; text-align: right; color: var(--ink);
    font-family: "Fira Sans Extra Condensed", sans-serif; }
  .holder-name { font-size: 34px; font-weight: 600; line-height: 40px; }
  .holder-title { font-size: 27px; font-weight: 400; line-height: 36px; }

  .contact { position: absolute; left: 49px; top: 383px; color: var(--ink);
    font-family: "Fira Sans Extra Condensed", sans-serif; font-size: 25px; line-height: 29.5px; list-style: none; }

  .tagline { position: absolute; left: 0; width: 100%; top: 518px; text-align: center; color: var(--ink);
    font-family: "Courgette", cursive; font-style: italic; font-size: 25px; letter-spacing: 0.3px; white-space: nowrap; }

  .dim { position: absolute; font-family: "Roboto", Arial, sans-serif; font-style: italic; font-size: 21px; color: var(--label); }
  .dim-height { left: 30px; top: 420px; transform: rotate(-90deg); transform-origin: center; width: 70px; text-align: center; }
  .dim-width { left: 574px; top: 827px; width: 80px; text-align: center; }
  .side-label { position: absolute; left: 509px; top: 912px; width: 200px; text-align: center;
    font-family: "Roboto", Arial, sans-serif; font-weight: 500; font-size: 46px; color: #000; }
</style>
</head>
<body>
<main class="sheet">
  <section class="card" aria-label="Business card front">
    <svg class="wordmark" viewBox="0 0 995 568" aria-label="Brightfield Renovation Works">
      <circle cx="148" cy="258" r="112" fill="var(--mark)" opacity="0.9"/>
      <text x="235" y="130" font-size="96" textLength="713" lengthAdjust="spacingAndGlyphs">BRIGHTFIELD</text>
      <text x="235" y="181" font-size="54" textLength="710" lengthAdjust="spacingAndGlyphs">RENOVATION WORKS</text>
    </svg>

    <div class="holder">
      <p class="holder-name">Maren Holt</p>
      <p class="holder-title">President</p>
    </div>

    <ul class="contact">
      <li>Office: 555-214-3380</li>
      <li>Mobile: 555-309-7716</li>
      <li>Email: marenholt@brightfieldrenovationworks.com</li>
      <li>Website: www.brightfieldrenovationworks.com</li>
    </ul>

    <p class="tagline">Crafting Lasting Trust and Renewing Houses...One Family at a Time.</p>
  </section>

  <p class="dim dim-height">2.0 in</p>
  <p class="dim dim-width">3.5 in</p>
  <p class="side-label">Front</p>
</main>
</body>
</html>
```